PACKAGING Pistacho Ice cream cup 500 ml

Ice cream PACKAGING round cup design

packing design for supermarkets displays

Focus in a premium new upmarket ice cream brand whit traditional ingredients and artisan traditionals flavors

1.- must be in : CMYK
2.- design in Photoshop CS6 or adobe illustrator CS6
3.- design must be in layers by element (name, picture , flavor, nutritiom fact, etc)
4.- 600 dpi resolution

Target Market(s)

upmarket ice cream consumers

Industry/Entity Type

Food Production

Colors
000000
474747
abd036
9bcb3c
fece3e

Requirements
Must have
• importatn highlights
• 5.-Text : HELADO PREMIUM
• 6.- Cup background : black dluxe
• 7.- Banner flavor text : PISTACHO
• 8.- Banner flavor color : Green whit lights efects and golden border lines
• 9.- Text : 500 ml
• 10.- picture : like ball icecream whit natural pistachos decoration.
• 11.- cup background waterbase waves
• 12 .- rectangle area 6cm width by 9cm high for nutritional information, ingredients and legal information

```html
<!DOCTYPE html>
<html lang="es">
<head>
<meta charset="utf-8">
<title>Helado Premium Pistachio – Cup Label</title>
<link href="https://fonts.googleapis.com/css2?family=Cinzel:wght@600&family=Montserrat:wght@600;800&display=swap" rel="stylesheet">
<style>
  :root {
    --canvas-bg: #e9ecec;
    --cup-black: #000000;
    --cup-charcoal: #1b1b1b;
    --wave-grey: #474747;
    --green-light: #abd036;
    --green-deep: #6f9a22;
    --green-mid: #9bcb3c;
    --gold: #fece3e;
    --gold-dark: #b8861c;
    --white: #ffffff;
  }
  html, body {
    margin: 0;
    padding: 0;
    width: 1138px;
    height: 1200px;
    overflow: hidden;
    background: var(--canvas-bg);
  }
  .canvas {
    position: relative;
    width: 1138px;
    height: 1200px;
  }
  .cup-label {
    position: absolute;
    left: 219px;
    top: 220px;
    width: 700px;
    height: 760px;
    overflow: hidden;
    border-radius: 6px;
    box-shadow: 0 10px 30px rgba(0,0,0,0.18);
  }
  .cup-label svg.label-art {
    position: absolute;
    inset: 0;
  }
  .brand {
    position: absolute;
    top: 120px;
    left: 0;
    width: 100%;
    display: flex;
    justify-content: center;
    align-items: center;
    gap: 12px;
    font-family: "Montserrat", sans-serif;
    font-weight: 800;
    font-size: 30px;
    color: var(--gold);
  }
  .brand-dot {
    width: 18px;
    height: 18px;
    border-radius: 50%;
    background: var(--gold);
  }
  .product-title {
    position: absolute;
    top: 245px;
    left: 0;
    width: 100%;
    text-align: center;
    font-family: "Cinzel", serif;
    font-weight: 600;
    font-size: 50px;
    letter-spacing: 6px;
    color: var(--white);
  }
  .volume {
    position: absolute;
    left: 50px;
    top: 420px;
    padding: 6px 24px;
    border: 3px solid var(--gold);
    border-radius: 30px;
    font-family: "Montserrat", sans-serif;
    font-weight: 800;
    font-size: 32px;
    color: var(--gold);
  }
  .flavor-photo {
    position: absolute;
    left: 330px;
    top: 330px;
    width: 340px;
    height: 250px;
    border-radius: 120px 120px 60px 60px;
    background: radial-gradient(ellipse at 45% 40%, #c9e6b4 0%, #a6d38f 55%, #8a7a4a 100%);
  }
  .flavor-name {
    position: absolute;
    left: 50px;
    top: 600px;
    font-family: "Montserrat", sans-serif;
    font-weight: 800;
    font-size: 60px;
    letter-spacing: 3px;
    color: var(--white);
  }
</style>
</head>
<body>
<main class="canvas">
  <section class="cup-label">
    <svg class="label-art" width="700" height="760" viewBox="0 0 700 760" aria-hidden="true">
      <defs>
        <linearGradient id="deluxeBlack" x1="0" y1="0" x2="1" y2="1">
          <stop offset="0" stop-color="var(--cup-charcoal)"/>
          <stop offset="0.6" stop-color="var(--cup-black)"/>
        </linearGradient>
        <linearGradient id="bannerGreen" x1="0" y1="1" x2="1" y2="0">
          <stop offset="0" stop-color="var(--green-deep)"/>
          <stop offset="0.45" stop-color="var(--green-light)"/>
          <stop offset="0.75" stop-color="var(--green-mid)"/>
          <stop offset="1" stop-color="var(--green-deep)"/>
        </linearGradient>
        <linearGradient id="goldLine" x1="0" y1="0" x2="1" y2="0">
          <stop offset="0" stop-color="var(--gold-dark)"/>
          <stop offset="0.5" stop-color="var(--gold)"/>
          <stop offset="1" stop-color="var(--gold-dark)"/>
        </linearGradient>
      </defs>
      <rect class="cup-background" width="700" height="760" fill="url(#deluxeBlack)"/>
      <g class="water-waves" fill="none" stroke="var(--wave-grey)" stroke-opacity="0.35" stroke-width="2">
        <path d="M-20 120 C120 60 220 200 360 130 S600 60 720 140"/>
        <path d="M-20 330 C100 260 240 380 380 310 S620 250 720 320"/>
        <path d="M-20 720 C120 660 260 760 420 690"/>
      </g>
      <path class="flavor-banner" d="M0 480 C250 480 480 410 700 230 L700 760 L0 760 Z" fill="url(#bannerGreen)"/>
      <path class="banner-gold-top" d="M0 480 C250 480 480 410 700 230" fill="none" stroke="url(#goldLine)" stroke-width="6"/>
      <path class="banner-gold-inner" d="M0 500 C260 500 500 430 700 260" fill="none" stroke="url(#goldLine)" stroke-width="2"/>
      <path class="banner-black-wedge" d="M380 760 C500 700 610 620 700 500 L700 760 Z" fill="var(--cup-black)"/>
      <path class="banner-gold-lower" d="M380 760 C500 700 610 620 700 500" fill="none" stroke="url(#goldLine)" stroke-width="4"/>
    </svg>

    <div class="brand"><span class="brand-dot"></span>Norte Helados</div>
    <h1 class="product-title" style="margin:0">HELADO PREMIUM</h1>
    <div class="volume">500 ml</div>
    <div class="flavor-photo" role="img" aria-label="Three scoops of pistachio ice cream with natural pistachio nuts"></div>
    <div class="flavor-name">PISTACHIO</div>
  </section>
</main>
</body>
</html>
```